Duel Business card

Want an edgy business card that shows both of our companies on each side of the card, OR both together with a cool design.

*Must be edgy: We have attached our two business logos. We are a bail bond and immigration bond company.

Would like the address on one side only.
Need Phone, cell, website, address, and Name

Company Name 1: Cellgate Release Partners
www.cellgatereleasepartners.example

Company Name 2: Borderline Surety Associates
www.borderlinesuretyassociates.example

These cards will need to be easily changeable so I can modify new employees

Target Market(s)

people in jail, takign imigrants out of jail and from being taken back to there country

Industry/Entity Type

Business

Requirements
Must have
• Include both logos attached

```html
<!DOCTYPE html>
<html lang="en">
<head>
<meta charset="utf-8">
<title>Borderline Surety Associates · Cellgate Release Partners — Business Card</title>
<link rel="stylesheet" href="https://fonts.googleapis.com/css2?family=Roboto:wght@300;900&display=swap">
<style>
  :root {
    --slate: #7f8ca2;
    --slate-deep: #22395f;
    --coral: #ef4b3c;
    --royal: #163a8a;
    --gold: #f2c230;
    --white: #ffffff;
    --seam: #c9d0dc;
  }
  * { box-sizing: border-box; margin: 0; padding: 0; }
  html, body {
    width: 1200px; height: 667px; overflow: hidden;
    background: var(--white);
  }
  .card {
    position: relative;
    width: 1200px; height: 667px;
    display: flex;
    font-family: "Roboto", Arial, sans-serif;
  }
  .side {
    position: relative;
    width: 600px; height: 667px;
    color: var(--white);
  }
  .side--immigration { background: var(--slate); border-right: 1px solid var(--seam); }
  .side--bail { background: var(--royal); }

  .brand {
    position: absolute;
    left: 0; right: 0;
    display: flex; flex-direction: column; align-items: center;
    text-align: center;
  }
  .brand__mark {
    border-radius: 50%;
    flex: none;
  }
  .brand__name {
    font-weight: 900;
    text-transform: uppercase;
  }

  .side--immigration .brand { top: 120px; }
  .side--immigration .brand__mark {
    width: 120px; height: 120px;
    background: var(--seam);
    margin-bottom: 28px;
  }
  .brand__name--immigration {
    font-size: 46px;
    line-height: 1.12;
    letter-spacing: 3px;
    color: var(--slate-deep);
  }

  .side--bail .brand { top: 150px; }
  .side--bail .brand__mark {
    width: 130px; height: 130px;
    background: var(--gold);
    margin-bottom: 30px;
  }
  .brand__name--bail {
    font-size: 50px;
    line-height: 1.08;
    letter-spacing: 1px;
    color: var(--white);
  }

  .contact {
    position: absolute;
    bottom: 18px;
    list-style: none;
    font-weight: 300;
    font-size: 28px;
    line-height: 40px;
  }
  .side--immigration .contact { left: 24px; }
  .side--bail .contact { right: 24px; text-align: right; }
  .contact__item { display: flex; align-items: center; gap: 10px; white-space: nowrap; }
  .side--bail .contact__item { justify-content: flex-end; }
  .contact__icon { width: 28px; height: 28px; flex: none; }
</style>
</head>
<body>
<main class="card">
  <section class="side side--immigration">
    <div class="brand">
      <div class="brand__mark" aria-hidden="true"></div>
      <p class="brand__name brand__name--immigration">Borderline<br>Surety<br>Associates</p>
    </div>
    <ul class="contact">
      <li class="contact__item">
        <svg class="contact__icon" viewBox="0 0 28 28" aria-hidden="true"><rect x="2" y="5" width="24" height="18" rx="2" fill="none" stroke="#fff" stroke-width="2"/><path d="M6 10h5v4H8v4H6zM14 9h6v3h3v5h-5v-3h-4z" fill="#fff"/></svg>
        <span>Address here</span>
      </li>
      <li class="contact__item">
        <svg class="contact__icon" viewBox="0 0 28 28" aria-hidden="true"><path d="M8 3l4 5-2.5 3c1.5 3 4 5.5 7 7l3-2.5 5 4-2.5 4C12 23 5 16 4 6z" fill="#fff"/></svg>
        <span>Phone here</span>
      </li>
      <li class="contact__item">
        <svg class="contact__icon" viewBox="0 0 28 28" aria-hidden="true"><circle cx="14" cy="14" r="11.5" fill="none" stroke="#fff" stroke-width="2"/><rect x="12.8" y="12" width="2.4" height="9" fill="#fff"/><circle cx="14" cy="8.5" r="1.6" fill="#fff"/></svg>
        <span>borderlinesuretyassociates.example</span>
      </li>
    </ul>
  </section>

  <section class="side side--bail">
    <div class="brand">
      <div class="brand__mark" aria-hidden="true"></div>
      <p class="brand__name brand__name--bail">Cellgate Release<br>Partners</p>
    </div>
    <ul class="contact">
      <li class="contact__item">
        <span>Name here</span>
        <svg class="contact__icon" viewBox="0 0 28 28" aria-hidden="true"><circle cx="14" cy="9" r="5" fill="#fff"/><path d="M4 25c0-6 4.5-9 10-9s10 3 10 9z" fill="#fff"/></svg>
      </li>
      <li class="contact__item">
        <span>Phone here</span>
        <svg class="contact__icon" viewBox="0 0 28 28" aria-hidden="true"><path d="M8 3l4 5-2.5 3c1.5 3 4 5.5 7 7l3-2.5 5 4-2.5 4C12 23 5 16 4 6z" fill="#fff"/></svg>
      </li>
      <li class="contact__item">
        <span>Cell here</span>
        <svg class="contact__icon" viewBox="0 0 28 28" aria-hidden="true"><rect x="8" y="2" width="12" height="24" rx="2.5" fill="none" stroke="#fff" stroke-width="2"/><circle cx="14" cy="22" r="1.5" fill="#fff"/></svg>
      </li>
      <li class="contact__item">
        <span>cellgatereleasepartners.example</span>
        <svg class="contact__icon" viewBox="0 0 28 28" aria-hidden="true"><circle cx="14" cy="14" r="11.5" fill="none" stroke="#fff" stroke-width="2"/><rect x="12.8" y="12" width="2.4" height="9" fill="#fff"/><circle cx="14" cy="8.5" r="1.6" fill="#fff"/></svg>
      </li>
    </ul>
  </section>
</main>
</body>
</html>
```